Packaging box design for start up candle company based in Sydney Australia

I need an eye catching box design for my candle company called Midnight Wickhouse. We specialise only in delicious cake and cocktail scented candles. I want to convey a sense of elegant whimsy.
I have a logo and a style guide which I'm happy with, but need to complete the brand with a stunning box design.
I'd like the same design for two different sized boxes.

```html
<!DOCTYPE html>
<html lang="en">
<head>
<meta charset="utf-8">
<title>Midnight Wickhouse – Sydney Box</title>
<link rel="stylesheet" href="https://fonts.googleapis.com/css2?family=Gilda+Display&family=Montserrat:wght@400&display=swap">
<style>
  :root {
    --page: #f2f2f2;
    --board: #d8dfe1;
    --ink: #231f20;
    --ink-soft: #3a3637;
    --accent: #e8806a;
    --art-teal: #6f9ea0;
    --art-pink: #e9b9cf;
    --art-purple: #9a5aa6;
    --art-slate: #4a4d52;
    --art-sand: #b89b86;
  }
  * { margin: 0; padding: 0; box-sizing: border-box; }
  html, body { width: 1200px; height: 1168px; overflow: hidden; background: var(--page); }
  .box-face {
    position: absolute; left: 100px; top: 39px;
    width: 1000px; height: 1090px;
    background: var(--board);
  }
  .artwork {
    position: absolute; left: 82px; top: 135px;
    width: 836px; height: 820px;
    background:
      linear-gradient(180deg, rgba(111,158,160,0.9) 0%, rgba(111,158,160,0) 30%),
      linear-gradient(90deg, var(--art-slate) 0%, var(--art-purple) 12%, var(--art-pink) 40%, var(--art-pink) 65%, var(--art-sand) 85%, var(--art-slate) 100%);
  }
  .label-panel {
    position: absolute; left: 87px; top: 127px;
    width: 662px; height: 608px;
    background: var(--board);
    border: 6px solid var(--ink);
  }
  .brand-name {
    position: absolute; left: 0; right: 0; top: 86px;
    text-align: center;
    font-family: "Gilda Display", serif;
    font-size: 34px; letter-spacing: 5px; line-height: 1.15;
    color: var(--ink);
  }
  .title-frame { position: absolute; left: 0; top: 0; width: 650px; height: 596px; }
  .city-name {
    position: absolute; left: 0; right: 0; top: 296px;
    text-align: center;
    font-family: "Gilda Display", serif;
    font-size: 128px; line-height: 1;
    color: var(--ink);
  }
  .skyline {
    position: absolute; left: 234px; top: 448px;
    width: 234px; height: 34px;
    background: linear-gradient(180deg, var(--ink-soft) 0%, var(--ink) 100%);
  }
  .tagline {
    position: absolute; left: 0; right: 0; top: 556px;
    text-align: center;
    font-family: "Montserrat", sans-serif;
    font-size: 22px; color: var(--ink);
  }
</style>
</head>
<body>
  <div class="box-face">
    <div class="artwork" role="img" aria-label="Abstract painted brushstrokes and splatters in teal, pink, purple, yellow and slate">
      <div class="label-panel">
        <div class="brand-name">MIDNIGHT<br>WICKHOUSE</div>
        <svg class="title-frame" viewBox="0 0 650 596" aria-hidden="true">
          <g fill="none" stroke="var(--ink)" stroke-width="2">
            <polyline points="288,266 68,266 68,467 203,467"/>
            <polyline points="362,266 586,266 586,473 484,473"/>
          </g>
          <circle cx="325" cy="252" r="38" fill="none" stroke="var(--accent)" stroke-width="1.5"/>
        </svg>
        <div class="city-name">Sydney</div>
        <div class="skyline" role="img" aria-label="Sydney city skyline silhouette illustration"></div>
        <div class="tagline">Cocktail Scented Candles</div>
      </div>
    </div>
  </div>
</body>
</html>
```